Clothing Brand E-Commerce Website Design

We would like you to provide an ecommerce design template in layered PSD for our clothing/fashion brand website called "TrelWick".
We want the site to have a simple but sleek design similar to the following sites:
http://www.pivorane.com/
http://corvatelle.com/
http://www.dulvenor.com/
We want it to look stunning and blow the example sites out of the water. For color scheme, please use your imagination and try to impress us with your creativity.
We like teal and beige pink, with teal dominant.
Teal #7AFFFF / #46C6C6
Beige/pink #FF7B7C / #C74646
We want you to develop the design for 3 pages:
1) Home Page
Samples:
http://www.pivorane.com/
http://corvatelle.com/
http://www.dulvenor.com/
2) Products List Page (e.g., lists all "Dresses" when category is selected)
http://www.pivorane.com/shop/casual-dresses
http://www.dulvenor.com/index.php?main_page=index&cPath=3
http://corvatelle.com/modest-dresses.html
http://www.quillmarsh.com/Product/Category.aspx?br=q47&category=dress_maxi
3) Product Detail Page (e.g., individual product page with "Add to Cart")
http://www.pivorane.com/shop/dresses/lumen-fern-dress
http://corvatelle.com/modest-dresses/modest-dress-tova.html
http://www.dulvenor.com/index.php?main_page=product_info&cPath=3&products_id=297
Industry/Entity Type
Fashion

```html
<!DOCTYPE html>
<html lang="en">
<head>
<meta charset="utf-8">
<title>TrelWick — Home</title>
<link rel="stylesheet" href="https://fonts.googleapis.com/css2?family=Open+Sans:wght@400;600&family=Noto+Serif:wght@400&display=swap">
<style>
  :root {
    --teal: #46C6C6;
    --teal-light: #7ADEDE;
    --pink: #FF7B7C;
    --red: #C74646;
    --pink-dark: #E86A6B;
    --ink: #444;
    --muted: #8c8c8c;
    --line: #dcdcdc;
    --sans: "Open Sans", Arial, sans-serif;
    --serif: "Noto Serif", Georgia, serif;
  }
  * { box-sizing: border-box; margin: 0; padding: 0; }
  html, body { width: 825px; height: 1200px; overflow: hidden; background: #fff; }
  .page { position: relative; width: 825px; height: 1200px; font-family: var(--sans); color: var(--ink); }
  .abs { position: absolute; }

  /* utility bar */
  .utility { left: 0; top: 0; width: 825px; height: 27px; background: linear-gradient(#fafafa, #ececec); border-bottom: 1px solid #dedede; }
  .utility-links { right: 88px; top: 8px; font-size: 7.5px; color: #555; display: flex; align-items: center; gap: 5px; letter-spacing: .2px; }
  .utility-links .sep { color: #888; }
  .cart-icon { width: 12px; height: 13px; }

  /* header */
  .logo { left: 89px; top: 44px; font-size: 28px; font-weight: 400; color: var(--teal); letter-spacing: .5px; }
  .search { left: 542px; top: 63px; width: 200px; height: 21px; border: 1px solid #ccc; background: #fff; display: flex; align-items: center; padding-left: 7px; gap: 6px; font-size: 8.5px; color: #999; }

  /* navigation */
  .nav { left: 0; top: 94px; width: 825px; height: 36px; background: linear-gradient(var(--teal-light), var(--teal)); }
  .nav ul { list-style: none; position: absolute; left: 86px; top: 0; height: 36px; display: flex; }
  .nav li { height: 36px; display: flex; align-items: center; justify-content: center; color: #fff; font-size: 10.5px; font-weight: 600; border-right: 1px solid rgba(255,255,255,.35); }
  .nav li:last-child { border-right: none; }

  /* hero */
  .hero { left: 0; top: 130px; width: 825px; height: 313px; background: linear-gradient(#fff 40%, #f1f1f1); border-bottom: 1px solid #ddd; }
  .hero-photo { left: 436px; top: 130px; width: 248px; height: 313px; background: linear-gradient(160deg, #e9d2c4 0%, #d8b7a4 35%, #2cc2c8 60%, #1fb3ba 100%); }
  .hero-title { left: 120px; top: 225px; font-family: var(--serif); font-size: 35px; color: var(--red); line-height: 1; }
  .hero-sub { left: 120px; top: 266px; font-family: var(--serif); font-size: 20.5px; color: var(--pink); line-height: 1; }
  .hero-copy { left: 122px; top: 296px; width: 290px; font-size: 9.5px; line-height: 15px; color: #a0a0a0; }
  .hero-arrow { top: 252px; width: 20px; height: 28px; }

  /* new arrivals */
  .section-title { left: 89px; top: 474px; font-size: 16px; color: #555; }
  .product { top: 500px; width: 120px; text-align: center; }
  .product-photo { width: 84px; height: 162px; margin: 0 auto; border-radius: 6px 6px 4px 4px; }
  .product-name { margin-top: 13px; font-size: 10px; color: var(--pink); }
  .product-desc { font-size: 7.5px; line-height: 13px; color: var(--muted); }
  .carousel-arrow { top: 570px; width: 16px; height: 36px; }
  .divider { left: 88px; top: 744px; width: 654px; height: 1px; background: var(--line); }

  /* category tiles */
  .tile { top: 770px; width: 207px; height: 150px; overflow: hidden; box-shadow: 0 1px 2px rgba(0,0,0,.15); }
  .tile-photo { position: absolute; inset: 0; }
  .tile-caption { position: absolute; left: 0; bottom: 0; width: 100%; height: 34px; display: flex; align-items: center; justify-content: space-between; padding: 0 11px 0 14px; font-family: var(--serif); font-size: 15px; color: #fff; }
  .caption-teal { background: rgba(70,198,198,.8); }
  .caption-pink { background: rgba(255,123,124,.82); }
  .caption-dark { color: #333; }
  .tile-go { width: 24px; height: 19px; }

  /* footer */
  .footer { left: 0; top: 982px; width: 825px; height: 178px; background: var(--pink); }
  .footer-col { top: 1010px; color: #fff; }
  .footer-col h3 { font-size: 13px; font-weight: 400; margin-bottom: 7px; }
  .footer-col li { list-style: none; font-size: 9px; line-height: 17px; padding-left: 2px; }
  .footer-rule { top: 1012px; width: 1px; height: 102px; background: rgba(255,255,255,.3); }
  .social { left: 507px; top: 1033px; display: flex; gap: 2.5px; }
  .social span { width: 18px; height: 18px; border-radius: 50%; background: #fff; display: block; }
  .legal { left: 0; top: 1160px; width: 825px; height: 40px; background: var(--pink-dark); }
  .legal p { position: absolute; left: 87px; top: 16px; font-size: 8px; color: #fde4e4; }
</style>
</head>
<body>
<div class="page">

  <!-- utility bar -->
  <div class="abs utility"></div>
  <div class="abs utility-links">
    <span>SIGN IN</span><span class="sep">|</span>
    <span>MY ACCOUNT</span><span class="sep">|</span>
    <svg class="cart-icon" viewBox="0 0 12 13"><rect x="0" y="0" width="12" height="13" rx="2" fill="#F5B300"/><path d="M3 4 q3 5 6 0" stroke="#fff" stroke-width="1.3" fill="none"/></svg>
    <span>MY CART</span><span class="sep">|</span>
    <span>CHECKOUT</span>
  </div>

  <!-- header -->
  <div class="abs logo">TrelWick</div>
  <div class="abs search">
    <svg width="10" height="10" viewBox="0 0 10 10"><circle cx="4" cy="4" r="3" stroke="#666" stroke-width="1.4" fill="none"/><line x1="6.3" y1="6.3" x2="9.3" y2="9.3" stroke="#666" stroke-width="1.6"/></svg>
    <span>Search</span>
  </div>

  <!-- navigation -->
  <nav class="abs nav">
    <ul>
      <li style="width:104px">NEW ARRIVALS</li>
      <li style="width:83px">CLOTHING</li>
      <li style="width:77px">DRESSES</li>
      <li style="width:65px">SHOES</li>
      <li style="width:70px">ABOUT</li>
      <li style="width:99px">ACCESSORIES</li>
      <li style="width:79px">SUPPORT</li>
      <li style="width:84px">CONTACT</li>
    </ul>
  </nav>

  <!-- hero -->
  <div class="abs hero"></div>
  <div class="abs hero-photo" role="img" aria-label="Model in a teal fitted dress"></div>
  <h1 class="abs hero-title">Its Fashion time</h1>
  <h2 class="abs hero-sub">Check latest Arrival Dresses</h2>
  <p class="abs hero-copy">Vivamus porttitor neque at volutpat rutruma purus nisi eleifend libero a tempus libero lectus feugiat felis Morbi</p>
  <svg class="abs hero-arrow" style="left:67px" viewBox="0 0 20 28"><path d="M16 2 L5 14 L16 26" stroke="#F0605F" stroke-width="6" fill="none"/></svg>
  <svg class="abs hero-arrow" style="left:737px" viewBox="0 0 20 28"><path d="M4 2 L15 14 L4 26" stroke="#F0605F" stroke-width="6" fill="none"/></svg>

  <!-- new arrivals -->
  <h2 class="abs section-title">NEW ARRIVALS</h2>
  <svg class="abs carousel-arrow" style="left:64px" viewBox="0 0 16 36"><path d="M14 2 L2 18 L14 34" stroke="var(--teal)" stroke-width="1.4" fill="none"/></svg>
  <svg class="abs carousel-arrow" style="left:746px" viewBox="0 0 16 36"><path d="M2 2 L14 18 L2 34" stroke="var(--teal)" stroke-width="1.4" fill="none"/></svg>

  <div class="abs product" style="left:94px">
    <div class="product-photo" role="img" aria-label="Navy lace sleeveless dress" style="background:linear-gradient(#3a3f86,#1f2466)"></div>
    <p class="product-name">Dress Tittle</p>
    <p class="product-desc">Etiam est nunc venenatis in<br>tristique eu imperdiet</p>
  </div>
  <div class="abs product" style="left:223px">
    <div class="product-photo" role="img" aria-label="Periwinkle high-low dress" style="background:linear-gradient(#8a9ee6,#5c70cc)"></div>
    <p class="product-name">Dress Tittle</p>
    <p class="product-desc">Etiam est nunc venenatis in<br>tristique eu imperdiet</p>
  </div>
  <div class="abs product" style="left:352px">
    <div class="product-photo" role="img" aria-label="Model in a white lace dress" style="background:linear-gradient(#e8dcd4,#f4f1ee)"></div>
    <p class="product-name">Dress Tittle</p>
    <p class="product-desc">Etiam est nunc venenatis in<br>tristique eu imperdiet</p>
  </div>
  <div class="abs product" style="left:481px">
    <div class="product-photo" role="img" aria-label="Model in a black cut-out dress" style="background:linear-gradient(#d8bfa8,#2a2a2a 45%,#1a1a1a)"></div>
    <p class="product-name">Dress Tittle</p>
    <p class="product-desc">Etiam est nunc venenatis in<br>tristique eu imperdiet</p>
  </div>
  <div class="abs product" style="left:610px">
    <div class="product-photo" role="img" aria-label="Red strapless chiffon dress on a form" style="background:linear-gradient(#e8323c,#f0606a)"></div>
    <p class="product-name">Dress Tittle</p>
    <p class="product-desc">Etiam est nunc venenatis in<br>tristique eu imperdiet</p>
  </div>

  <div class="abs divider"></div>

  <!-- category tiles -->
  <div class="abs tile" style="left:87px">
    <div class="tile-photo" role="img" aria-label="Model in a teal blazer against weathered wood" style="background:linear-gradient(#b8aa9a,#8f8478 45%,#3fc4c0)"></div>
    <div class="tile-caption caption-teal"><span>Summer Arrivals</span>
      <svg class="tile-go" viewBox="0 0 24 19"><rect x=".75" y=".75" width="22.5" height="17.5" fill="none" stroke="#fff" stroke-width="1.5"/><path d="M6 9.5 H17 M13 5.5 L17 9.5 L13 13.5" stroke="#fff" stroke-width="2" fill="none"/></svg>
    </div>
  </div>
  <div class="abs tile" style="left:312px">
    <div class="tile-photo" role="img" aria-label="Model in a purple top by a brick wall" style="background:linear-gradient(90deg,#8a7464,#c9c2bb 70%,#e4e0dc)"></div>
    <div class="tile-caption caption-teal caption-dark"><span>Fashion &amp; Party</span>
      <svg class="tile-go" viewBox="0 0 24 19"><rect x=".75" y=".75" width="22.5" height="17.5" fill="none" stroke="#fff" stroke-width="1.5"/><path d="M6 9.5 H17 M13 5.5 L17 9.5 L13 13.5" stroke="#fff" stroke-width="2" fill="none"/></svg>
    </div>
  </div>
  <div class="abs tile" style="left:538px">
    <div class="tile-photo" role="img" aria-label="Bride in a lace gown before a damask backdrop" style="background:linear-gradient(#a9a6b8,#c4c0cc 60%,#e2d8da)"></div>
    <div class="tile-caption caption-pink"><span>Wedding Special</span>
      <svg class="tile-go" viewBox="0 0 24 19"><rect x=".75" y=".75" width="22.5" height="17.5" fill="none" stroke="#fff" stroke-width="1.5"/><path d="M6 9.5 H17 M13 5.5 L17 9.5 L13 13.5" stroke="#fff" stroke-width="2" fill="none"/></svg>
    </div>
  </div>

  <!-- footer -->
  <footer>
    <div class="abs footer"></div>
    <div class="abs footer-col" style="left:86px"><h3>COMPANY</h3><ul><li>New Arrivals</li><li>About Us</li><li>Clothings</li><li>Shoes</li><li>Bags &amp; Accessories</li></ul></div>
    <div class="abs footer-rule" style="left:198px"></div>
    <div class="abs footer-col" style="left:225px"><h3>FEATURES</h3><ul><li>Featured Products</li><li>Speical</li><li>What's New</li><li>Gift &amp; Coupons</li></ul></div>
    <div class="abs footer-rule" style="left:330px"></div>
    <div class="abs footer-col" style="left:361px"><h3>INFORMATION</h3><ul><li>Shipping &amp; Return</li><li>Privacy Policy</li><li>Sitemap</li><li>My Account</li></ul></div>
    <div class="abs footer-rule" style="left:478px"></div>
    <div class="abs footer-col" style="left:507px"><h3>FIND US ON</h3></div>
    <div class="abs social"><span></span><span></span><span></span><span></span></div>
    <div class="abs legal"><p>© 2014 Company Name &nbsp;All right reserved &nbsp;Term of Use</p></div>
  </footer>

</div>
</body>
</html>
```